Meridian Handsets business card design

I would like to see some designs for a business card for Meridian Handsets. I would like the business card to be double sided. It will need to have a similar colour / look and feel to our website www.meridianhandsets.com.au I have also attached our latest flyer. Final designs to be handed over in Photoshop format so that I can edit the business card when needed please.

Industry/Entity Type

Business

Contact Information for Business Card

Gavin Thornley
sales@meridianhandsets.com.au
Business Development Manager
ph: (08) 6197 5821
www.meridianhandsets.com.au

Font styles to use
Serif
Sans Serif

Requirements
Must have
• If you could please utilise our colour scheme as seen on our website and the attached flyer.
• I would also like the final design to be in a Photoshop format so that I can edit it when needed please.

```html
<!DOCTYPE html>
<html lang="en">
<head>
<meta charset="utf-8">
<title>Meridian Handsets – Business Card</title>
<link href="https://fonts.googleapis.com/css2?family=Montserrat:wght@400;600;700&display=swap" rel="stylesheet">
<style>
  :root {
    --page-bg: #d6d8da;
    --card-bg: #f1f1f1;
    --ink: #2a2a2a;
    --muted: #8a8a8a;
    --brand-blue: #1677b6;
    --steel-blue: #3f7db5;
    --teal: #14a086;
  }
  html, body {
    margin: 0;
    width: 1200px;
    height: 800px;
    overflow: hidden;
    background: var(--page-bg);
    font-family: "Montserrat", sans-serif;
    color: var(--ink);
  }
  .canvas {
    width: 1200px;
    height: 800px;
    display: flex;
    flex-direction: column;
    align-items: center;
    justify-content: center;
    gap: 30px;
  }
  .card {
    position: relative;
    width: 620px;
    height: 354px;
    background: var(--card-bg);
    box-shadow: 0 6px 18px rgba(0,0,0,0.18);
    overflow: hidden;
  }
  .wordmark {
    font-weight: 700;
    color: var(--brand-blue);
    white-space: nowrap;
  }
  .card-front .wordmark {
    position: absolute;
    left: 0;
    right: 0;
    top: 112px;
    text-align: center;
    font-size: 50px;
  }
  .accent-band {
    position: absolute;
    left: 0;
    width: 620px;
  }
  .card-front .accent-band {
    top: 268px;
    height: 32px;
    background: linear-gradient(90deg, var(--teal) 0%, var(--steel-blue) 30%, var(--brand-blue) 75%, var(--teal) 100%);
  }
  .card-back .wordmark {
    position: absolute;
    left: 28px;
    top: 82px;
    font-size: 28px;
  }
  .contact {
    position: absolute;
    right: 48px;
    top: 72px;
    display: grid;
    grid-template-columns: auto auto;
    column-gap: 10px;
  }
  .contact-person, .contact-details {
    grid-column: 1;
    text-align: right;
    padding-right: 10px;
    border-right: 2px dotted var(--ink);
  }
  .person-name {
    font-weight: 700;
    font-size: 15px;
    margin: 0;
  }
  .person-title {
    font-size: 8px;
    color: var(--muted);
    margin: 2px 0 0;
    letter-spacing: 0.3px;
  }
  .contact-details {
    margin-top: 26px;
    font-size: 12px;
    line-height: 15px;
  }
  .contact-labels {
    grid-column: 2;
    margin-top: 26px;
    font-size: 11px;
    font-weight: 600;
    line-height: 15px;
    text-align: right;
  }
  .contact-details p, .contact-labels p { margin: 0; }
  .card-back .accent-band {
    top: 274px;
    height: 22px;
    background: linear-gradient(90deg, var(--ink) 0%, var(--teal) 25%, var(--steel-blue) 50%, var(--steel-blue) 100%);
  }
</style>
</head>
<body>
<main class="canvas">

  <section class="card card-front" aria-label="Business card front">
    <div class="wordmark">Meridian Handsets</div>
    <div class="accent-band" role="img" aria-label="Decorative teal and blue stripe band"></div>
  </section>

  <section class="card card-back" aria-label="Business card back">
    <div class="wordmark">Meridian Handsets</div>
    <div class="contact">
      <div class="contact-person">
        <p class="person-name">Gavin Thornley</p>
        <p class="person-title">Business Development Manager</p>
      </div>
      <div class="contact-details">
        <p>(08) 6197 5821</p>
        <p>sales@meridianhandsets.com.au</p>
        <p>www.meridianhandsets.com.au</p>
      </div>
      <div class="contact-labels">
        <p>Phone</p>
        <p>E-Mail</p>
        <p>Web</p>
      </div>
    </div>
    <div class="accent-band" role="img" aria-label="Decorative dark, teal and blue stripe band"></div>
  </section>

</main>
</body>
</html>
```